Steady at Heart: Renew Your Team Through the 6 Habits of Balance

I'm looking for a design that is clean, like the book "Look Sideways" by Milo Brecken. The book is about the principles of organic farming so I am looking for a color scheme that fits that image.
https://www.pagelantern.example/Look-Sideways-Value-Seeing-Other-ebook/dp/Q47K520ZTR/ref=sr_1_3?crid=58XQ2PL07ZV4M&keywords=milo+brecken&qid=1638739111&s=books&sprefix=milo+%2Cstripbooks%2C371&sr=1-3

I don't want a dark color scheme. I prefer a white or cream book with a bold font.

This book is a good example of what I am looking for:

https://www.pagelantern.example/Lamp-Small-Notes-Painting-Days/dp/0912736458/ref=rtpb_2/731-5529043-4417082?pd_rd_w=mq8z3&pf_rd_p=21c9e047-385b-4f7d-a1c2-6e30b8d7f914&pf_rd_r=KP3T8QZ2207LM4NX1VA5&pd_rd_r=e63a1f20-7c4d-4a91-b5e8-09f2d1c7a6e3&pd_rd_wg=3kR2x&pd_rd_i=0912736458&psc=1

Target Market(s)

CEOs and business owners who want to increase the trust in their brands

Industry/Entity Type

Management and Leadership

Colors
00AB8E
00BBA5
67D7C9
C6EFE9
E9F9F6
59FF00
82FF00
B8FF75
E3FFCB
F4FFEA
FFF300
FFF600
FEFA6F
FFFEC7
FFFEE8
FFC000
F8CF3A
FAE287
FDF2CF
FEFAEE

Requirements
Must have
• Author's name is: Harold Vesterby
Nice to have
• I have indicated some books that I like. I would be good to have a simple image such as an apple core or the earth's core or some other image of "core" but not absolutely necessary.
Should not have
• I don't want it to have a dark cover or be too heavy

```html
<!DOCTYPE html>
<html lang="en">
<head>
<meta charset="utf-8">
<title>Steady at Heart – Book Cover</title>
<link href="https://fonts.googleapis.com/css2?family=Anton&family=Oswald:wght@600&family=Questrial&display=swap" rel="stylesheet">
<style>
  :root {
    --ink: #0a0a0a;
    --orange: #f26a1b;
    --sky: #6dcff6;
    --sky-light: #bfe8fb;
    --mist: #eef8fd;
    --paper: #ffffff;
    --rule: #8a8a8a;
    --fruit: #f39a1e;
    --water: #3f8fd0;
  }
  * { box-sizing: border-box; margin: 0; padding: 0; }
  html, body { width: 1200px; height: 1000px; overflow: hidden; background: var(--paper); }
  .canvas { position: relative; width: 1200px; height: 1000px; }

  .spread { position: absolute; left: 187px; top: 22px; width: 990px; height: 730px; display: flex; }

  /* Back cover */
  .back {
    position: relative; width: 476px; height: 100%;
    background: linear-gradient(180deg, var(--sky) 0%, #8fdaf8 55%, var(--sky-light) 100%);
    padding: 44px 52px 0 61px;
    font-family: "Questrial", sans-serif; color: var(--ink);
  }
  .back-copy { position: relative; z-index: 2; }
  .back-title { font-family: "Anton", sans-serif; font-size: 37px; line-height: 1; text-align: center; letter-spacing: .5px; }
  .back-subtitle { font-family: "Oswald", sans-serif; font-weight: 600; color: var(--orange); text-align: center; font-size: 17px; line-height: 1.15; margin-top: 12px; text-transform: uppercase; }
  .back-subtitle .big { font-size: 21px; display: block; }
  .blurb { margin-top: 12px; font-size: 9.4px; line-height: 1.62; letter-spacing: -0.1px; }
  .blurb p { margin-bottom: 7px; }
  .blurb ul { list-style: none; margin-bottom: 7px; }
  .blurb li { position: relative; padding-left: 11px; }
  .blurb li::before { content: ""; position: absolute; left: 0; top: 5px; width: 5px; height: 5px; border-radius: 50%; background: var(--ink); }
  .divider { border: 0; border-top: 1px solid var(--rule); margin: 9px 0 12px; }
  .bio { font-size: 9.4px; line-height: 1.62; letter-spacing: -0.1px; }
  .bio strong { font-weight: 700; }
  .back-art {
    position: absolute; left: 0; right: 0; top: 495px; bottom: 0; z-index: 1;
    background:
      radial-gradient(ellipse 22% 38% at 52% 68%, var(--fruit) 0%, #f7b247 70%, transparent 72%),
      radial-gradient(ellipse 60% 40% at 45% 72%, rgba(63,143,208,.55), transparent 75%);
  }

  /* Spine */
  .spine {
    width: 27px; height: 100%;
    background: linear-gradient(180deg, var(--sky) 0%, var(--sky-light) 100%);
    display: flex; flex-direction: column; align-items: center; justify-content: space-between;
    padding: 34px 0 62px;
    font-family: "Oswald", sans-serif; font-weight: 600; font-size: 9px; letter-spacing: 1.6px;
  }
  .spine span { writing-mode: vertical-rl; white-space: nowrap; }
  .spine .sep { color: var(--ink); }
  .spine .sub { color: var(--orange); }

  /* Front cover */
  .front {
    position: relative; width: 487px; height: 100%;
    background: radial-gradient(ellipse 70% 60% at 60% 45%, var(--paper) 0%, var(--mist) 45%, #bfe6f8 100%);
    text-align: center; color: var(--ink);
  }
  .front-title { font-family: "Anton", sans-serif; line-height: .9; padding-top: 50px; position: relative; z-index: 1; }
  .front-title .l1 { display: block; font-size: 96px; letter-spacing: 1px; }
  .front-title .l2 { display: block; font-size: 70px; margin-top: 2px; }
  .front-title .l3 { display: block; font-size: 150px; letter-spacing: 1px; }
  .front-art {
    position: absolute; left: 80px; top: 230px; width: 330px; height: 330px; z-index: 2;
    background:
      radial-gradient(circle at 50% 62%, var(--fruit) 0%, #f7a935 28%, transparent 30%),
      radial-gradient(ellipse 60% 35% at 50% 68%, rgba(63,143,208,.5), transparent 75%);
  }
  .front-subtitle { position: absolute; left: 0; right: 0; top: 578px; font-family: "Oswald", sans-serif; font-weight: 600; color: var(--orange); text-transform: uppercase; line-height: 1.12; font-size: 20px; }
  .front-subtitle .big { display: block; font-size: 24px; }
  .front-author { position: absolute; left: 0; right: 0; top: 655px; font-family: "Anton", sans-serif; font-size: 42px; letter-spacing: 1px; }
</style>
</head>
<body>
<main class="canvas">
  <section class="spread">
    <article class="back">
      <div class="back-copy">
        <h2 class="back-title">STEADY AT HEART</h2>
        <p class="back-subtitle">Renew your team through<span class="big">the 6 habits of balance</span></p>
        <div class="blurb">
          <p>Do you need to increase repeat sales? Do you wonder why other customers do not buy your products at all? Have you invested in certification, but it does not seem to help?</p>
          <p>This book helps you understand why you are experiencing results far below your sales potential. And it shows you how to become the brand your customers love and tell their friends about.</p>
          <p>This book will give you a step by step plan to help you:</p>
          <ul>
            <li>Attract and keep customers by connecting them with the larger community</li>
            <li>Craft authentic products that do what they say they will do and delight customers</li>
            <li>Increase profitability by connecting your brand to the community and the environment</li>
          </ul>
          <p>Thriving businesses are so much more than just “hello” and a goodbye. When you create a brand that resonates deeply with your customers and offer products they want and need, they will keep coming back and help you grow.</p>
          <p>And it is easier than you think. Steady at Heart shows you how.</p>
        </div>
        <hr class="divider">
        <p class="bio"><strong>HAROLD VESTERBY</strong> is CEO of Verdanta Trust, the leader in organic certification for New Zealand. Born in Madison, Wisconsin, he has over 25 years working in Japan, New Zealand and Asia helping high-value brands such as Maple Hearth Foods, Fernvale, Ridgewood Farm, Summit Crunch, Sakura Pantry, Kiwora, Hoshino Drinks and Greenrow Kitchen access foreign markets and achieve organic certification. He lives with his family in Wellington, New Zealand.</p>
      </div>
      <div class="back-art" role="img" aria-label="Photo of a leafy orange half submerged in splashing water"></div>
    </article>

    <aside class="spine">
      <span><span class="sep">STEADY AT HEART &nbsp;| &nbsp;</span><span class="sub">RENEW YOUR TEAM THROUGH THE 6 HABITS OF BALANCE</span></span>
      <span>HAROLD VESTERBY</span>
    </aside>

    <article class="front">
      <h1 class="front-title"><span class="l1">STEADY</span><span class="l2">AT</span><span class="l3">HEART</span></h1>
      <div class="front-art" role="img" aria-label="Photo of an orange with leaves sliced by a splash of clear water"></div>
      <p class="front-subtitle">Renew your team through<span class="big">the 6 habits of balance</span></p>
      <p class="front-author">HAROLD VESTERBY</p>
    </article>
  </section>
</main>
</body>
</html>
```